Audio-Visual & Video Communications Business Requires a Cutting-edge Business Card Design

LinkVessel is a new Audio-Visual & Video Communications company in Cape Town, South Africa that is looking for a cutting-edge business card design. We sell these products to the Corporate, Education & Hospitality markets and will also host an Online Shop for companies and individuals to purchase our products online.

We are already using the following two colours in our logo and draft website. Please incorporate these colours into the design. Please note that our website is still in the design stage if you need to visit it. Green #a0ce4e & Dark Grey #333333.
Updates

Hi,

Please note that I have uploaded our logo in an .eps format.

Target Market(s)

Corporate Companies, Education Institutions & Hospitality Markets

Industry/Entity Type

Business

Requirements
Nice to have
• It would be great if you could incorporate the services that we offer.

1. Consultation & Design
2. Project Management
3. Supply & Installation
4. Onsite Support Personal
5. Online Shop

```html
<!DOCTYPE html>
<html lang="en">
<head>
<meta charset="utf-8">
<title>LinkVessel Business Card Options</title>
<link href="https://fonts.googleapis.com/css2?family=Michroma&family=Open+Sans:wght@700&display=swap" rel="stylesheet">
<style>
  :root {
    --green: #a2c75c;
    --charcoal: #414241;
    --mid-grey: #6a6b6a;
    --white: #ffffff;
    --label: #2b2b2b;
  }
  html, body {
    margin: 0;
    padding: 0;
    width: 1200px;
    height: 868px;
    overflow: hidden;
    background: var(--white);
  }
  .sheet {
    position: relative;
    width: 1200px;
    height: 868px;
  }
  .column-label, .row-label {
    position: absolute;
    font-family: "Michroma", sans-serif;
    font-weight: 400;
    font-size: 19px;
    letter-spacing: 0.5px;
    color: var(--label);
    -webkit-text-stroke: 0.8px var(--label);
    line-height: 1;
  }
  .column-label { top: 102px; transform: translateX(-50%); }
  .column-label--front { left: 342px; }
  .column-label--back { left: 881px; }
  .row-label {
    left: 58px;
    transform: translate(-50%, -50%) rotate(-90deg);
    white-space: nowrap;
  }
  .row-label--one { top: 281px; }
  .row-label--two { top: 604px; }

  .card {
    position: absolute;
    width: 538px;
    height: 318px;
  }
  .card--green { background: var(--green); }
  .card--charcoal { background: var(--charcoal); }
  .card--o1-front { left: 73px; top: 123px; }
  .card--o1-back { left: 612px; top: 123px; }
  .card--o2-front { left: 73px; top: 445px; }
  .card--o2-back { left: 612px; top: 445px; }

  .brand-dot {
    position: absolute;
    left: 50%;
    transform: translateX(-50%);
    border-radius: 50%;
  }
  .brand-name {
    position: absolute;
    left: 0;
    right: 0;
    text-align: center;
    font-family: "Open Sans", sans-serif;
    font-weight: 700;
    letter-spacing: -0.5px;
    line-height: 1;
    margin: 0;
  }
  .card--o1-front .brand-dot {
    top: 92px; width: 84px; height: 84px; background: var(--mid-grey);
  }
  .card--o1-front .brand-name {
    top: 193px; font-size: 35px; color: var(--green);
  }
  .card--o2-front .brand-dot {
    top: 64px; width: 122px; height: 122px; background: var(--white);
  }
  .card--o2-front .brand-name {
    top: 213px; font-size: 46px; color: var(--white);
  }

  .services {
    position: absolute;
    left: 0;
    right: 0;
    margin: 0;
    padding: 0;
    list-style: none;
    text-align: center;
    font-family: "Michroma", sans-serif;
    font-size: 11.5px;
    line-height: 16.5px;
    color: var(--white);
    letter-spacing: -0.2px;
  }
  .services .sep {
    display: inline-block;
    font-size: 9px;
    margin: 0 5px;
    vertical-align: 1px;
  }
  .card--o1-front .services { top: 266px; }
  .card--o2-back .services { top: 266px; }
</style>
</head>
<body>
<main class="sheet">
  <div class="column-label column-label--front">FRONT</div>
  <div class="column-label column-label--back">BACK</div>
  <div class="row-label row-label--one">OPTION 1</div>
  <div class="row-label row-label--two">OPTION 2</div>

  <section class="card card--charcoal card--o1-front">
    <span class="brand-dot"></span>
    <h1 class="brand-name">LinkVessel</h1>
    <ul class="services">
      <li>Consultation &amp; Design<span class="sep">|</span>Project Management</li>
      <li>Supply &amp; Installation<span class="sep">|</span>Onsite Support Personal<span class="sep">|</span>Online Shop</li>
    </ul>
  </section>
  <section class="card card--green card--o1-back"></section>

  <section class="card card--green card--o2-front">
    <span class="brand-dot"></span>
    <h2 class="brand-name">LinkVessel</h2>
  </section>
  <section class="card card--charcoal card--o2-back">
    <ul class="services">
      <li>Consultation &amp; Design<span class="sep">|</span>Project Management</li>
      <li>Supply &amp; Installation<span class="sep">|</span>Onsite Support Personal<span class="sep">|</span>Online Shop</li>
    </ul>
  </section>
</main>
</body>
</html>
```